Solvane Travel Planners needs an bold logo and business card design

Thanks you all for helping me with this project your assistance is appriciated
I am starting a home based travel agency and I need a bold and eye catching logo and business card designed.
I want to convey a sense of FREEDOM, expertise, customer service for travel customers
Solvane travel planners is a full service travel agency focused on customer service and adding value to a vacation and travel planning.
my idea is for a card that looks like an cruise ship boarding pass or passport with stamps with a back drop of beautiful beach scene, resort hotel and happiness.
The logo should be eye catching, unique but give a sense of freedom and it should be travel related
We want to give customers a sense of Freedom from travel planning, freedom from researching cruises and hotels and freedom to enjoy a wonderful cost effective vacation.

Target Market(s)

Customers considering travel for vacations, family reunions, business and weddings

Industry/Entity Type

Travel Industry

Contact Information for Business Card

Solvane Travel Planners
Marcus Helbrook Owner
MHelbrook@SolvaneTravelPlanners.com
SolvaneTravelPlanners.com
(555) 214-7830

Logo Text

“One’s destination is never a place, but a new way of seeing things.”

Font styles to use
Serif

Colors
85cae6
0492cd
ec1f27
e667a6
b768aa
33b8a4

Requirements
Must have
• The Logo you create should be on the busoness card
• should be clean, easy to read and attractive
• something you that would make you want to work with a travel agent
Nice to have
• should have cruise ship, hotel on the card or something that conveys travel
Should not have
• Should not have the american flag
• no yellow on the card

```html
<!DOCTYPE html>
<html lang="en">
<head>
<meta charset="utf-8">
<title>Solvane Travel Planners – Business Card</title>
<link rel="stylesheet" href="https://fonts.googleapis.com/css2?family=Gelasio:wght@400;700&display=swap">
<style>
  :root {
    --backdrop: #d4d4d4;
    --card-white: #ffffff;
    --plum: #b04a9c;
    --ink: #000000;
    --teal: #33a58f;
    --sky: #85cae6;
    --rose: #e667a6;
    --text-light: #ffffff;
  }
  * { margin: 0; padding: 0; box-sizing: border-box; }
  html, body {
    width: 992px;
    height: 1200px;
    overflow: hidden;
    background: var(--backdrop);
    font-family: "Gelasio", Georgia, serif;
  }
  .canvas {
    position: relative;
    width: 992px;
    height: 1200px;
  }
  .card {
    position: absolute;
    left: 99px;
    width: 807px;
    height: 461px;
    overflow: hidden;
  }
  .card--front { top: 104px; background: var(--card-white); }
  .card--back { top: 624px; background: var(--ink); }

  .card__wave {
    position: absolute;
    inset: 0;
    width: 807px;
    height: 461px;
  }
  .wave__shadow { fill: var(--ink); }
  .wave__band { fill: var(--plum); }

  .brand-name {
    position: absolute;
    color: var(--teal);
    font-weight: 700;
    line-height: 1.05;
  }
  .card--front .brand-name {
    left: 0;
    width: 807px;
    top: 168px;
    text-align: center;
    font-size: 36px;
  }
  .card--back .brand-name {
    left: 36px;
    top: 34px;
    font-size: 46px;
  }

  .scene-art {
    position: absolute;
    left: 150px;
    top: 160px;
    width: 620px;
    height: 290px;
    border-radius: 28px;
    background:
      radial-gradient(ellipse at 30% 60%, rgba(230,103,166,0.75), rgba(230,103,166,0) 60%),
      radial-gradient(ellipse at 85% 35%, rgba(51,184,164,0.75), rgba(51,184,164,0) 60%),
      linear-gradient(180deg, rgba(133,202,230,0.15), rgba(133,202,230,0.45));
  }

  .holder {
    position: absolute;
    left: 30px;
    top: 368px;
    color: var(--text-light);
  }
  .holder__name { font-size: 34px; font-weight: 400; line-height: 1.1; }
  .holder__role { font-size: 21px; font-weight: 700; margin-top: 4px; }

  .contacts {
    position: absolute;
    right: 34px;
    top: 344px;
    list-style: none;
    color: var(--text-light);
    font-size: 19px;
  }
  .contacts__item {
    display: flex;
    align-items: center;
    justify-content: flex-end;
    height: 33px;
    gap: 14px;
  }
  .contacts__icon {
    width: 15px;
    height: 15px;
    flex: none;
  }
  .contacts__icon rect { fill: var(--text-light); }
  .contacts__icon .glyph { fill: var(--plum); stroke: var(--plum); }
</style>
</head>
<body>
<main class="canvas">

  <section class="card card--front" aria-label="Business card front">
    <svg class="card__wave" viewBox="0 0 807 461" aria-hidden="true">
      <path class="wave__shadow" d="M0,240 C170,318 380,322 520,272 C660,222 760,132 807,56 L807,461 L0,461 Z"/>
      <path class="wave__band" d="M0,262 C170,330 370,326 510,292 C655,252 762,142 807,48 L807,461 L0,461 Z"/>
    </svg>

    <h1 class="brand-name">Solvane<br>Travel Planners</h1>

    <div class="holder">
      <p class="holder__name">Marcus Helbrook</p>
      <p class="holder__role">Owner</p>
    </div>

    <ul class="contacts">
      <li class="contacts__item">
        <span>(555) 214-7830</span>
        <svg class="contacts__icon" viewBox="0 0 15 15" aria-hidden="true">
          <rect width="15" height="15" rx="2"/>
          <path class="glyph" d="M3,5 h9 v2 h-2 v-1 h-5 v1 h-2 z M4,8 h7 l1,4 h-9 z"/>
        </svg>
      </li>
      <li class="contacts__item">
        <span>SolvaneTravelPlanners.com</span>
        <svg class="contacts__icon" viewBox="0 0 15 15" aria-hidden="true">
          <rect width="15" height="15" rx="2"/>
          <circle class="glyph" cx="7.5" cy="7.5" r="4.5" fill="none" stroke-width="1.6"/>
          <path class="glyph" d="M3,7.5 h9 M7.5,3 v9" stroke-width="1.2" fill="none"/>
        </svg>
      </li>
      <li class="contacts__item">
        <span>MHelbrook@SolvaneTravelPlanners.com</span>
        <svg class="contacts__icon" viewBox="0 0 15 15" aria-hidden="true">
          <rect width="15" height="15" rx="2"/>
          <rect class="glyph" x="3" y="4.5" width="9" height="6"/>
          <path d="M3,4.5 L7.5,8 L12,4.5" fill="none" stroke="#ffffff" stroke-width="1"/>
        </svg>
      </li>
    </ul>
  </section>

  <section class="card card--back" aria-label="Business card back">
    <h2 class="brand-name">Solvane<br>Travel Planners</h2>
    <div class="scene-art" role="img" aria-label="Illustration of a cruise ship on waves beside palm trees"></div>
  </section>

</main>
</body>
</html>
```